New business card with our logo

we finalized our logo with the help of pixel harbor - now we need a business card using that logo. we are a metal service center providing raw steel and metal products for fabricating, contractors, artists, etc. we have the wording for the back of the card figured out (attached, no deviations from text please), just need help putting it all together.
would like the look of steel somehow incorporated in the design ... would like the black part of the logo to be steel or silver color (the S & BRANLEY)
Other font styles liked:
- calibri, arial, similar to those, modern looking
Colors
Designer to choose colors to be used in the design.
Requirements
Must have
- Back of card must haves are attached (no deviations from wording please).
- FRONT of card:
- logo
- address
- name
- office tel
- cell
- fax
- website
- address
Nice to have
- incorporate the look of steel or element of steel somehow
- names of the staff on front not in all caps, i.e. Rosvita not ROSVITA
- this industry is more industrial, not coffee or flower shop so design should be aligned with that
- design should be classic and tasteful

```html
<!DOCTYPE html>
<html lang="en">
<head>
<meta charset="utf-8">
<title>Branley Steel – Business Card</title>
<link rel="stylesheet" href="https://fonts.googleapis.com/css2?family=Arimo:ital,wght@0,400;0,700;1,700&display=swap">
<style>
  :root {
    --backdrop: #2f3338;
    --card: #ffffff;
    --brand-blue: #1670b8;
    --ink: #2a2a2a;
    --ink-soft: #555a60;
    --rule-blue: #8fbbe0;
    --rule-grey: #8a8d91;
  }
  * { margin: 0; padding: 0; box-sizing: border-box; }
  html, body {
    width: 1200px; height: 1141px; overflow: hidden;
    background: var(--backdrop);
    font-family: "Arimo", Arial, sans-serif;
    color: var(--ink);
  }
  .card {
    position: absolute; left: 232px; width: 730px; height: 414px;
    background: var(--card); border-radius: 34px; overflow: hidden;
  }
  .card--front { top: 119px; }
  .card--back { top: 570px; }

  .brand { position: absolute; left: 0; right: 0; top: 44px; height: 76px;
    display: flex; align-items: center; justify-content: center; gap: 18px; }
  .brand__dot { width: 64px; height: 64px; border-radius: 50%; background: var(--brand-blue); }
  .brand__name { font-size: 48px; font-weight: 400; color: var(--ink); letter-spacing: 0.5px; }

  .person { position: absolute; left: 0; right: 0; top: 156px; text-align: center; }
  .person__name { font-size: 35px; font-weight: 700; color: var(--brand-blue); line-height: 1.15; }
  .person__title { font-size: 16px; color: var(--ink); margin-top: 1px; }

  .divider { position: absolute; height: 1px; }
  .divider--front { left: 42px; right: 44px; top: 265px; background: var(--rule-blue); }
  .divider--back { left: 108px; right: 107px; top: 224px; background: var(--rule-grey); }

  .contacts { position: absolute; left: 42px; top: 276px; list-style: none; }
  .contacts li { display: flex; align-items: center; height: 25.7px; font-size: 17px; }
  .contacts svg { width: 16px; height: 16px; margin-right: 18px; fill: var(--brand-blue); flex: none; }
  .address { position: absolute; right: 42px; top: 276px; font-size: 17px; line-height: 25.7px; }

  .web-band { position: absolute; left: 0; right: 0; bottom: 0; height: 31px;
    background: var(--brand-blue); color: #fff; font-size: 17px;
    display: flex; align-items: center; justify-content: center; }

  .service { position: absolute; left: 0; right: 0; top: 145px; text-align: center; }
  .service__heading { font-size: 30px; font-weight: 700; letter-spacing: 1px; color: var(--ink); -webkit-text-stroke: 0.6px var(--ink); }
  .service__tasks { font-size: 17px; color: var(--ink-soft); margin-top: 6px; letter-spacing: 0.5px; }

  .products { position: absolute; left: 0; right: 0; top: 239px; text-align: center;
    font-size: 17.5px; font-weight: 700; line-height: 27px; }
  .tagline { position: absolute; left: 0; right: 0; top: 354px; text-align: center;
    font-size: 23px; font-weight: 700; font-style: italic; }
  .sep { margin: 0 4px; }
</style>
</head>
<body>

<section class="card card--front">
  <div class="brand">
    <span class="brand__dot"></span>
    <span class="brand__name">BRANLEY STEEL</span>
  </div>
  <div class="person">
    <div class="person__name">Nadir Oussama Belkadi</div>
    <div class="person__title">Managing Director</div>
  </div>
  <div class="divider divider--front"></div>
  <ul class="contacts">
    <li><svg viewBox="0 0 16 16" aria-hidden="true"><path d="M1 6c0-2 3-3 7-3s7 1 7 3v1h-4V5.5H5V7H1z M3 8h10l1 6H2z M6 10h4v2H6z"/></svg>000-000-000</li>
    <li><svg viewBox="0 0 16 16" aria-hidden="true"><path d="M3 1l3 0 1 4-2 1.5c1 2 2.5 3.5 4.5 4.5L11 9l4 1v3c0 1-1 2-2 2C7 15 1 9 1 3c0-1 1-2 2-2z"/></svg>000-000-000</li>
    <li><svg viewBox="0 0 16 16" aria-hidden="true"><path d="M5 1h6v5H5z M2 7h12v8H2z M4 9h3v1.5H4z M9 9h3v1.5H9z"/></svg>000-000-000</li>
    <li><svg viewBox="0 0 16 16" aria-hidden="true"><path d="M1 3h14v1.5L8 9 1 4.5z M1 6.3l7 4.5 7-4.5V13H1z"/></svg>info@branleysteel.com</li>
  </ul>
  <div class="address">Rue Verte 18, Liège 4000, Belgium</div>
  <div class="web-band">www.branleysteel.com</div>
</section>

<section class="card card--back">
  <div class="brand">
    <span class="brand__dot"></span>
    <span class="brand__name">BRANLEY STEEL</span>
  </div>
  <div class="service">
    <div class="service__heading">METAL SERVICE CENTER</div>
    <div class="service__tasks">CUT <span class="sep">•</span> SHEAR <span class="sep">•</span> PUNCH <span class="sep">•</span> LIGHT FAB</div>
  </div>
  <div class="divider divider--back"></div>
  <div class="products">
    <div>Structural Steel <span class="sep">•</span> Stainless &amp; Aluminum</div>
    <div>Building Components <span class="sep">•</span> Rebar <span class="sep">•</span> Deckling .....and more!</div>
  </div>
  <div class="tagline">Cut to size, Pick-up or Deliverid!</div>
</section>

</body>
</html>
```